Start-up consultancy in Healthcare Space requiring clean and crisp website design

I am the founder of a start-up consultancy to improve access to medicines and healthcare around the globe. My primary product are consulting services to both the public sector and the private sector to work on: improved healthcare delivery, the right price for medicines and addressing challenges in emerging markets. As the sector is fairly conservative, I need a clean and very professional website as is should signal competence in the sector. Therefore, I like shades of white and green but there should be a link to healthcare. Please see the logo that is featured on my business cards.

Target Market(s)

Ministry of Health, Pharmaceutical companies, Emerging Markets (Latin America, Middle East, Eastern Europe, Asia)

Industry/Entity Type

Healthcare

Coding

Coded - Design and coding required

Number of Pages Required

5+ page

Font styles to use
Serif

Colors

Designer to choose colors to be used in the design.

Requirements
Must have
• About Section
• Services Section
• Blog Section
• The website design should also portray the solution for access to healthcare and highlight my ability to help clients with that.
• The website will be hosted on a CMS and should therefore be easy to adjust. I would prefer wordpress but open to any suggestions as I have my own webspace.
• I quite like these websites:
• https://www.tevluma.com/why-tevluma
• https://home.quillfernwell.com/
Nice to have
• I like to see some creative thinking with the theme of healthcare.
Should not have
• The design should not feature too many hospitals or pills etc. as this is really not my focus.

```html
<!DOCTYPE html>
<html lang="en">
<head>
<meta charset="utf-8">
<title>Veridane Consulting</title>
<link href="https://fonts.googleapis.com/css2?family=Roboto:wght@300;400;500;700&display=swap" rel="stylesheet">
<style>
:root{
  --green:#0b5e2f;
  --green-bright:#169c52;
  --green-pale:#dde6e0;
  --ink:#2b2f36;
  --text:#4a4d52;
  --muted:#8a8d92;
  --gray-bg:#f4f4f4;
  --line:#e4e4e4;
  --footer:#2e2f3e;
  --footer-bottom:#272835;
  --white:#ffffff;
}
*{box-sizing:border-box;margin:0;padding:0}
html,body{width:1200px;height:2651px;overflow:hidden}
body{font-family:"Roboto",sans-serif;color:var(--text);background:var(--white);position:relative}
.abs{position:absolute}

/* header */
.site-header{left:0;top:0;width:1200px;height:65px;background:var(--white)}
.brand{left:88px;top:18px;display:flex;align-items:center;gap:10px}
.brand-square{width:30px;height:30px;border:2px solid var(--green)}
.brand-name{font-size:22px;font-weight:500;color:var(--green);letter-spacing:.5px}
.main-nav{right:90px;top:18px;display:flex;align-items:center;gap:30px;font-size:12px;color:var(--ink);letter-spacing:.3px}
.btn-signup{background:var(--green);color:var(--white);padding:10px 20px;font-weight:500}

/* hero */
.hero{left:0;top:65px;width:1200px;height:553px;background:linear-gradient(100deg,#4a4d3c 0%,#7a6c5c 30%,#6f7760 55%,#8e9a86 80%,#5f6b55 100%)}
.hero-shade{left:0;top:65px;width:1200px;height:553px;background:linear-gradient(90deg,rgba(0,0,0,0) 40%,rgba(0,0,0,.25) 100%)}
.hero-copy{left:600px;top:305px;width:428px;text-align:center;color:var(--white)}
.hero-kicker{font-size:22px;font-weight:500;letter-spacing:.5px}
.hero-title{font-size:35px;font-weight:400;margin-top:2px;letter-spacing:.5px}
.btn-hero{display:inline-block;margin-top:14px;background:var(--green);color:var(--white);font-size:11px;font-weight:500;padding:11px 22px}
.hero-arrow{width:32px;height:66px;top:309px;background:rgba(0,0,0,.45);display:flex;align-items:center;justify-content:center}

/* services */
.gray-band{left:0;top:618px;width:1200px;height:525px;background:var(--gray-bg)}
.service-card{top:565px;height:216px;background:var(--white);border:1px solid var(--line);text-align:center;font-size:13.5px;color:var(--ink);line-height:18px}
.service-icon{width:60px;height:60px;margin:52px auto 22px;border-radius:8px}
.about{left:0;top:880px;width:1200px;text-align:center}
.section-title{font-size:30px;font-weight:400;color:var(--ink)}
.about p{width:830px;margin:18px auto 0;font-size:13px;line-height:23px}
.btn-pale{display:inline-block;margin-top:20px;background:var(--green-pale);color:var(--ink);font-size:11px;font-weight:500;padding:12px 24px}

/* solutions */
.solutions-title{left:0;top:1210px;width:1200px;text-align:center}
.solution-card{top:1272px;width:325px;height:341px;background:var(--white);border:1px solid var(--line);border-bottom:3px solid var(--green)}
.solution-photo{height:189px}
.solution-card h3{font-size:15px;font-weight:500;color:var(--green);margin:34px 24px 8px}
.solution-card p{font-size:12px;line-height:20px;margin:0 24px}

/* blog */
.blog-band{left:0;top:1702px;width:1200px;height:448px;background:var(--green-bright)}
.blog-title{left:0;top:1762px;width:1200px;text-align:center;color:var(--white)}
.blog-card{left:88px;top:1824px;width:1022px;height:247px;background:var(--white)}
.blog-photo{left:88px;top:1824px;width:324px;height:247px;background:linear-gradient(135deg,#f3f1ee 0%,#e6e0dc 50%,#c9b9b0 100%)}
.blog-date{left:371px;top:1905px;width:78px;height:88px;background:var(--green);color:var(--white);text-align:center;padding-top:10px}
.blog-date b{display:block;font-size:36px;font-weight:500;line-height:40px}
.blog-date span{font-size:11px;font-weight:500;letter-spacing:.5px}
.blog-body{left:518px;top:1890px;width:555px}
.blog-body h3{font-size:20px;font-weight:400;color:var(--ink)}
.blog-meta{display:flex;gap:18px;font-size:11px;color:var(--ink);margin:8px 0 16px}
.blog-meta span{display:flex;align-items:center;gap:6px}
.blog-body p{font-size:12px;line-height:21px}
.blog-arrow{top:1940px;width:32px;height:30px;background:#9a9a9a;display:flex;align-items:center;justify-content:center}

/* cta */
.cta{left:0;top:2230px;width:1200px;text-align:center}
.cta p{font-size:12px;line-height:21px;margin-top:12px}
.btn-dark{display:inline-block;margin-top:16px;background:var(--green);color:var(--white);font-size:11px;font-weight:500;padding:12px 30px}

/* footer */
.site-footer{left:0;top:2449px;width:1200px;height:154px;background:var(--footer)}
.footer-brand{left:88px;top:2520px;display:flex;align-items:center;gap:10px}
.footer-brand .brand-square{border-color:var(--white)}
.footer-brand .brand-name{color:var(--white)}
.footer-nav{right:90px;top:2497px;display:flex;gap:28px;font-size:11px;color:var(--white);font-weight:500}
.footer-rule{left:860px;top:2534px;width:250px;height:1px;background:#4a4c5c}
.footer-social{right:90px;top:2552px;display:flex;gap:12px}
.footer-social span{width:20px;height:20px;border-radius:50%;background:#3d3f50}
.footer-bottom{left:0;top:2603px;width:1200px;height:48px;background:var(--footer-bottom);color:var(--white);font-size:11px}
.footer-bottom .copy{left:88px;top:17px}
.footer-bottom .legal{right:90px;top:17px}
.to-top{left:1148px;top:2589px;width:32px;height:32px;border-radius:50%;background:var(--green-bright);display:flex;align-items:center;justify-content:center}
</style>
</head>
<body>

<header class="site-header abs">
  <div class="brand abs"><span class="brand-square"></span><span class="brand-name">VERIDANE</span></div>
  <nav class="main-nav abs">
    <span>ABOUT</span><span>SERVICES</span><span>SOLUTIONS</span><span>BLOG</span>
    <span class="btn-signup">SIGN UP</span>
  </nav>
</header>

<div class="hero abs" role="img" aria-label="Smiling mother lifting her young daughter outdoors among trees"></div>
<div class="hero-shade abs"></div>
<div class="hero-arrow abs" style="left:0"><svg width="8" height="12"><path d="M6 1 1 6l5 5" stroke="#fff" stroke-width="1.5" fill="none"/></svg></div>
<div class="hero-arrow abs" style="left:1168px"><svg width="8" height="12"><path d="M2 1l5 5-5 5" stroke="#fff" stroke-width="1.5" fill="none"/></svg></div>
<div class="hero-copy abs">
  <div class="hero-kicker">WELCOME TO</div>
  <div class="hero-title">VERIDANE CONSULTING</div>
  <span class="btn-hero">READ MORE</span>
</div>

<div class="gray-band abs"></div>

<div class="service-card abs" style="left:88px;width:334px">
  <div class="service-icon" role="img" aria-label="Illustration of a group of people" style="background:linear-gradient(180deg,#e0a277 0%,#6f8fb8 100%)"></div>
  Public Consulting<br>Services
</div>
<div class="service-card abs" style="left:433px;width:332px">
  <div class="service-icon" role="img" aria-label="Illustration of a business advisor" style="background:linear-gradient(180deg,#c99a78 0%,#3d5678 100%)"></div>
  Private Consulting<br>Services
</div>
<div class="service-card abs" style="left:777px;width:333px">
  <div class="service-icon" role="img" aria-label="Illustration of scattered medicines" style="background:linear-gradient(135deg,#e7a5a3 0%,#f3f1ee 55%,#a9bcd6 100%)"></div>
  Access to Healthcare<br>Services
</div>

<section class="about abs">
  <h2 class="section-title">About Us</h2>
  <p>Lorem ipsum dolor sit amet, consectetuer adipiscing elit aenean commodo ligula eget dolor aenean massa. Cum sociis<br>natoque penatibus et magnis dis parturient montes, nascetur ridiculus mus. Donec quam felis ultricies nec, pellentesque eu pretium quis<br>sem nulla consequat massa quis enim.</p>
  <span class="btn-pale">READ MORE</span>
</section>

<h2 class="section-title solutions-title abs">Our Solutions</h2>
<article class="solution-card abs" style="left:88px">
  <div class="solution-photo" role="img" aria-label="Mother and daughter drawing together on a bed" style="background:linear-gradient(135deg,#9fd4dc 0%,#e9e4e0 50%,#f2eee8 100%)"></div>
  <h3>Employers</h3>
  <p>Nam quam nunc blandit vel luctus pulvinar, hendrerit id, lorem maecenas nec odio et ante tincidunt tempus donec</p>
</article>
<article class="solution-card abs" style="left:438px">
  <div class="solution-photo" role="img" aria-label="Two colleagues smiling at a laptop in an office" style="background:linear-gradient(135deg,#e9ecef 0%,#d9d3cf 50%,#b33a3a 100%)"></div>
  <h3>Health Plans</h3>
  <p>Nam quam nunc blandit vel luctus pulvinar, hendrerit id, lorem maecenas nec odio et ante tincidunt tempus donec</p>
</article>
<article class="solution-card abs" style="left:786px">
  <div class="solution-photo" role="img" aria-label="Person in a plaid shirt using a smartphone outdoors" style="background:linear-gradient(90deg,#3b5a4a 0%,#7a8a6a 40%,#d8dcc0 100%)"></div>
  <h3>Health Systems</h3>
  <p>Nam quam nunc blandit vel luctus pulvinar, hendrerit id, lorem maecenas nec odio et ante tincidunt tempus donec</p>
</article>

<div class="blog-band abs"></div>
<h2 class="section-title blog-title abs" style="color:var(--white)">Latest Blog</h2>
<div class="blog-card abs"></div>
<div class="blog-photo abs" role="img" aria-label="Capsules and a thermometer on a white surface"></div>
<div class="blog-date abs"><b>27</b><span>APRIL</span></div>
<div class="blog-arrow abs" style="left:88px"><svg width="8" height="12"><path d="M6 1 1 6l5 5" stroke="#fff" stroke-width="1.5" fill="none"/></svg></div>
<div class="blog-arrow abs" style="left:1078px"><svg width="8" height="12"><path d="M2 1l5 5-5 5" stroke="#fff" stroke-width="1.5" fill="none"/></svg></div>
<div class="blog-body abs">
  <h3>Standard post with preview picture</h3>
  <div class="blog-meta">
    <span><svg width="12" height="12"><circle cx="6" cy="4" r="3" fill="none" stroke="#169c52"/><path d="M1 12a5 5 0 0 1 10 0" fill="none" stroke="#169c52"/></svg>Posted By : Admin</span>
    <span><svg width="13" height="12"><ellipse cx="6.5" cy="5.5" rx="5.5" ry="4.5" fill="none" stroke="#169c52"/></svg>Comments : 7</span>
    <span><svg width="11" height="12"><rect x="1" y="1" width="9" height="10" fill="none" stroke="#169c52"/></svg>Tag : Business</span>
  </div>
  <p>Lorem ipsum dolor sit amet, consectetuer adipiscing elit. Aenean commodo ligula eget dolor. Aenean massa. Cum sociis natoque penatibus et magnis dis parturient montes, nascetur ridiculus mus. Donec quam felis, ultricies nec, pellentesque eu, pretiu</p>
</div>

<section class="cta abs">
  <h2 class="section-title">Let's get started</h2>
  <p>Lorem ipsum dolor sit amet, consectetuer adipiscing elit. Aenean commodo ligula eget dolor.<br>Aenean massa cum sociis natoque penatibus et magnis dis parturient .</p>
  <span class="btn-dark">CONTACT US</span>
</section>

<footer class="site-footer abs"></footer>
<div class="footer-brand abs"><span class="brand-square"></span><span class="brand-name">VERIDANE</span></div>
<nav class="footer-nav abs"><span>ABOUT</span><span>SERVICES</span><span>SOLUTIONS</span><span>BLOG</span></nav>
<div class="footer-rule abs"></div>
<div class="footer-social abs"><span></span><span></span><span></span><span></span></div>
<div class="footer-bottom abs">
  <span class="copy abs">© 2017 Veridane Consulting | All Right Reserved</span>
  <span class="legal abs">Terms &amp; COnditions &nbsp; | &nbsp; Privacy Policy</span>
</div>
<div class="to-top abs"><svg width="10" height="7"><path d="M1 6l4-4 4 4" stroke="#fff" stroke-width="1.5" fill="none"/></svg></div>

</body>
</html>
```